Wine label for family vineyard start-up

Brand new family vineyard needs a new label:

The information we need on the label is the following:
- Merlot & Cabernet (variety)
- Poggio Varessa (location)
- 2016 (vintage)

The style of the label should be graphic / minimal / masculine.

This is a wine made by three 35yr old guys

Target Market(s)

young & urban

Industry/Entity Type

Vineyard

Logo Text

Merlot & Cabernet / Poggio Varessa / 2016

Font styles to use
Sans Serif

Requirements
Must have
• clearly legible
• aesthetically pleasing [minimalist]
• sans serif

```html
<!DOCTYPE html>
<html lang="en">
<head>
<meta charset="utf-8">
<title>Tre Colli – 2016 Poggio Varessa Merlot &amp; Cabernet label options</title>
<link href="https://fonts.googleapis.com/css2?family=Sniglet&family=Meddon&family=Didact+Gothic&family=Arimo:wght@400&display=swap" rel="stylesheet">
<style>
  :root {
    --wine: #9b1a0e;
    --cream: #fffdd2;
    --page: #ffffff;
  }
  html, body {
    margin: 0;
    padding: 0;
    width: 846px;
    height: 1200px;
    overflow: hidden;
    background: var(--page);
  }
  .sheet {
    position: relative;
    width: 846px;
    height: 1200px;
  }
  .label {
    position: absolute;
    width: 406px;
    height: 582px;
    box-sizing: border-box;
    background: var(--cream);
    border: 8px solid var(--wine);
    color: var(--wine);
    text-align: center;
  }
  .label::after {
    content: "";
    position: absolute;
    inset: 5px;
    border: 3px solid var(--wine);
    pointer-events: none;
  }
  .label--rounded  { left: 10px;  top: 10px;  font-family: "Sniglet", sans-serif; }
  .label--script   { left: 429px; top: 10px;  font-family: "Meddon", cursive; }
  .label--gothic   { left: 10px;  top: 603px; font-family: "Didact Gothic", sans-serif; }
  .label--caps     { left: 429px; top: 603px; font-family: "Arimo", sans-serif; }

  .brand {
    position: absolute;
    left: 0;
    right: 0;
    top: 134px;
    height: 210px;
    display: flex;
    flex-direction: column;
    align-items: center;
    justify-content: center;
    gap: 18px;
    font-size: 46px;
    line-height: 1;
  }
  .brand__mark {
    width: 22px;
    height: 22px;
    background: var(--wine);
  }
  .label--script .brand { font-size: 36px; }
  .label--caps .brand { text-transform: uppercase; font-size: 40px; letter-spacing: 2px; }

  .vintage {
    position: absolute;
    left: 0;
    right: 0;
    font-size: 30px;
    line-height: 30px;
  }
  .details {
    position: absolute;
    left: 0;
    right: 0;
    margin: 0;
  }
  .details span { display: block; }

  .label--rounded .vintage { top: 393px; }
  .label--rounded .details { top: 443px; font-size: 31px; line-height: 41px; }

  .label--script .vintage { top: 395px; font-size: 17px; line-height: 20px; }
  .label--script .details { top: 433px; font-size: 24px; line-height: 46px; }

  .label--gothic .vintage { top: 391px; font-size: 34px; line-height: 34px; }
  .label--gothic .details { top: 443px; font-size: 36px; line-height: 45px; }

  .label--caps .vintage { top: 392px; font-size: 32px; line-height: 32px; }
  .label--caps .details { top: 440px; font-size: 26px; line-height: 49px; text-transform: uppercase; }
</style>
</head>
<body>
<main class="sheet">
  <section class="label label--rounded">
    <div class="brand"><span class="brand__mark"></span><span class="brand__name">Tre Colli</span></div>
    <div class="vintage">2016</div>
    <p class="details"><span>Poggio Varessa</span><span>Merlot &amp; Cabernet</span></p>
  </section>

  <section class="label label--script">
    <div class="brand"><span class="brand__mark"></span><span class="brand__name">Tre Colli</span></div>
    <div class="vintage">2016</div>
    <p class="details"><span>Poggio Varessa</span><span>Merlot &amp; Cabernet</span></p>
  </section>

  <section class="label label--gothic">
    <div class="brand"><span class="brand__mark"></span><span class="brand__name">Tre Colli</span></div>
    <div class="vintage">2016</div>
    <p class="details"><span>Poggio Varessa</span><span>Merlot &amp; Cabernet</span></p>
  </section>

  <section class="label label--caps">
    <div class="brand"><span class="brand__mark"></span><span class="brand__name">Tre Colli</span></div>
    <div class="vintage">2016</div>
    <p class="details"><span>Merlot / Cabernet</span><span>Poggio Varessa</span></p>
  </section>
</main>
</body>
</html>
```